Android Game Graphics
Puzzle Game Buttons/Background
I'm developing a puzzle game for android and I need a fun/colorful background and several buttons. I have attached sketches of the three screens I need graphics for.
The winning logo must "pop" like the "fuzzy otters" graphics. The graphics need to be fun and colorful, but I have no formal requirements. The game is a clone of the classic game "Glyphwalk". You can see/play the original game here: http://marlowjpenfield.com/android/games/glyphwalk.swf Below I have sketches of the three screens in the game, please make these with colorful graphics and buttons. For the first and second images, make sure the background image has "Quill Quest" somewhere spanning the back. For the third image, the one with the letters, make all of the letters/tiles the same color. Wood color like tilzor would probably be the best, but I'm open to suggestions. Also where "Quill Quest" is on the third image, make some sort of cartoony logo. I was thinking maybe the word formed from some sort of cartoony worm with glasses, but again, it's up to you. Please make all of the buttons, including the letters individually and high res because they will eventually be used on a 10 inch (1280 x 800 resolution tablet). Screen 1: http://img811.pixelcrate.net/i/introscreen1.png/ Screen 2: http://img827.pixelcrate.net/i/selectgame2.png/ Screen 3: http://img573.pixelcrate.net/i/gameplay3.png/ Basically, make the three images above how you think the game and menu should look. The resolution in the attached images is 854 x 480, but make sure you make them for a higher res tablet.

```html
<!DOCTYPE html>
<html lang="en">
<head>
<meta charset="utf-8">
<title>Quill Quest – Main Menu</title>
<link rel="stylesheet" href="https://fonts.googleapis.com/css2?family=Luckiest+Guy&display=swap">
<style>
  :root {
    --page: #ffffff;
    --stone-light: #f3dd98;
    --stone: #e3c275;
    --stone-dark: #b48a3a;
    --stone-edge: #8f6a28;
    --field-center: #f0f57a;
    --field-mid: #c2ea6e;
    --field-edge: #7fd480;
    --wood: #c89b60;
    --wood-light: #ddb985;
    --wood-dark: #7a5428;
    --nail: #5e5e5e;
    --ink: #1c1006;
    --green: #3fd12e;
    --orange: #ff9a1a;
    --blue: #2d5bf0;
    --red: #ff2a2a;
    --logo: #f7941d;
    --mascot-a: #6fc3d8;
    --mascot-b: #eaa98a;
    --ledge: #c49a4e;
  }
  * { margin: 0; padding: 0; box-sizing: border-box; }
  html, body { width: 1200px; height: 758px; overflow: hidden; background: var(--page); }
  .menu-screen {
    position: relative; width: 1200px; height: 758px;
    font-family: "Luckiest Guy", "Arial Black", Impact, sans-serif;
  }
  .stone-frame {
    position: absolute; left: 10px; top: 10px; width: 1180px; height: 724px;
    border: 5px solid var(--stone-edge); border-radius: 30px;
    background:
      radial-gradient(circle at 8% 12%, var(--stone-light) 0 3%, transparent 9%),
      radial-gradient(circle at 92% 88%, var(--stone-light) 0 3%, transparent 9%),
      radial-gradient(circle at 50% 2%, var(--stone-light) 0 2%, transparent 7%),
      radial-gradient(circle at 50% 98%, var(--stone-light) 0 2%, transparent 7%),
      linear-gradient(135deg, var(--stone) 0%, var(--stone-dark) 50%, var(--stone) 100%);
  }
  .play-field {
    position: absolute; left: 48px; top: 44px; width: 1104px; height: 648px;
    border-radius: 60px 44px 70px 50px;
    border: 6px solid var(--stone-dark);
    box-shadow: inset 0 0 0 3px var(--stone-edge);
    background: radial-gradient(ellipse at 55% 50%, var(--field-center) 0%, var(--field-mid) 50%, var(--field-edge) 100%);
  }
  .game-title {
    position: absolute; left: 76px; top: 104px; width: 300px;
    font-size: 80px; font-weight: 900; line-height: .95;
    color: var(--logo); text-align: center; text-transform: uppercase;
  }
  .mascot-art {
    position: absolute; left: 36px; top: 318px; width: 330px; height: 394px;
    border-radius: 40px 40px 16px 28px;
    background: linear-gradient(180deg, var(--mascot-a) 0%, var(--mascot-b) 55%, var(--ledge) 100%);
  }
  .menu-button { position: absolute; width: 312px; height: 150px; }
  .menu-button svg { position: absolute; inset: 0; }
  .menu-button span {
    position: absolute; inset: 0; display: flex; align-items: center; justify-content: center;
    font-size: 38px; font-weight: 900; text-transform: uppercase; letter-spacing: 1px;
    -webkit-text-stroke: 6px var(--ink); paint-order: stroke fill;
  }
  .btn-time { left: 384px; top: 165px; }
  .btn-instructions { left: 744px; top: 165px; }
  .btn-freeplay { left: 384px; top: 432px; }
  .btn-quit { left: 744px; top: 432px; }
  .btn-time span { color: var(--green); }
  .btn-instructions span { color: var(--orange); font-size: 31px; }
  .btn-freeplay span { color: var(--blue); }
  .btn-quit span { color: var(--red); }
</style>
</head>
<body>
<main class="menu-screen">
  <div class="stone-frame" role="img" aria-label="Rocky sandstone cobble border framing the menu"></div>
  <div class="play-field"></div>

  <div class="mascot-art" role="img" aria-label="Cartoon worm mascot with a backpack giving a thumbs up on a rocky ledge"></div>
  <h1 class="game-title">Quill Quest</h1>

  <nav>
    <a class="menu-button btn-time">
      <svg viewBox="0 0 312 150" aria-hidden="true">
        <polygon points="6,10 306,4 302,146 10,140" fill="var(--wood)" stroke="var(--wood-dark)" stroke-width="6"/>
        <line x1="10" y1="72" x2="302" y2="74" stroke="var(--wood-light)" stroke-width="4"/>
        <circle cx="22" cy="22" r="5" fill="var(--nail)"/><circle cx="290" cy="18" r="5" fill="var(--nail)"/>
        <circle cx="24" cy="128" r="5" fill="var(--nail)"/><circle cx="288" cy="132" r="5" fill="var(--nail)"/>
      </svg>
      <span>Time Trial</span>
    </a>
    <a class="menu-button btn-instructions">
      <svg viewBox="0 0 312 150" aria-hidden="true">
        <polygon points="8,6 304,12 300,140 6,146" fill="var(--wood)" stroke="var(--wood-dark)" stroke-width="6"/>
        <line x1="8" y1="76" x2="302" y2="72" stroke="var(--wood-light)" stroke-width="4"/>
        <circle cx="22" cy="20" r="5" fill="var(--nail)"/><circle cx="290" cy="24" r="5" fill="var(--nail)"/>
        <circle cx="22" cy="132" r="5" fill="var(--nail)"/><circle cx="288" cy="128" r="5" fill="var(--nail)"/>
      </svg>
      <span>Instructions</span>
    </a>
    <a class="menu-button btn-freeplay">
      <svg viewBox="0 0 312 150" aria-hidden="true">
        <polygon points="4,8 308,6 304,144 8,146" fill="var(--wood)" stroke="var(--wood-dark)" stroke-width="6"/>
        <line x1="8" y1="74" x2="304" y2="76" stroke="var(--wood-light)" stroke-width="4"/>
        <circle cx="20" cy="20" r="5" fill="var(--nail)"/><circle cx="292" cy="20" r="5" fill="var(--nail)"/>
        <circle cx="22" cy="132" r="5" fill="var(--nail)"/><circle cx="290" cy="132" r="5" fill="var(--nail)"/>
      </svg>
      <span>Freeplay</span>
    </a>
    <a class="menu-button btn-quit">
      <svg viewBox="0 0 312 150" aria-hidden="true">
        <polygon points="6,6 306,10 308,142 4,146" fill="var(--wood)" stroke="var(--wood-dark)" stroke-width="6"/>
        <line x1="6" y1="74" x2="306" y2="74" stroke="var(--wood-light)" stroke-width="4"/>
        <circle cx="20" cy="20" r="5" fill="var(--nail)"/><circle cx="292" cy="22" r="5" fill="var(--nail)"/>
        <circle cx="20" cy="132" r="5" fill="var(--nail)"/><circle cx="292" cy="130" r="5" fill="var(--nail)"/>
      </svg>
      <span>Quit</span>
    </a>
  </nav>
</main>
</body>
</html>
```